Exciting Personal Development Book Cover: TURN LUMA UP!

Design a Book Cover for my personal development book.
Title: Turn LUMA Up!
Author: Marcus Tillet
Tagline: A real-life solution to get unstuck and break free

My picture must make up the front cover as I need to build my brand and people should recognise me on book shelves. Bold and catchy. How you do it is up to you. There must be space for a short testimonial from a famous person who is currently reading my book. I uploaded a sample of what I made in Photoshop but I don't have design skills.

I've added a PDF of my book so you can read the chapter index and introduction to get a sense of the content.

Target Market(s)

Personal Development Self-Help Market

Industry/Entity Type

Personal Development

Font styles to use
Serif
Sans Serif

Requirements
Must have
• My picture as hero image on cover.
Nice to have
• Must have Title, Tagline and my author name. If possible LUMA stands for 'Ownership, Vision & Action' If there is a way to fit this somewhere great. If it's too much then it can go somewhere on the back.

```html
<!DOCTYPE html>
<html lang="en">
<head>
<meta charset="utf-8">
<title>Turn LUMA Up! – Book Cover</title>
<link href="https://fonts.googleapis.com/css2?family=Bebas+Neue&display=swap" rel="stylesheet">
<style>
  :root {
    --page-bg: #e4e8ec;
    --cover-grey: #76797c;
    --cover-grey-light: #84878a;
    --navy: #131a5e;
    --white: #ffffff;
    --photo-light: #d9d6d3;
    --photo-mid: #a99385;
    --photo-dark: #5b4a42;
  }
  * { margin: 0; padding: 0; box-sizing: border-box; }
  html, body {
    width: 1200px;
    height: 848px;
    overflow: hidden;
    background: var(--page-bg);
  }
  body {
    position: relative;
    font-family: "Bebas Neue", "Arial Narrow", sans-serif;
  }
  .book-cover {
    position: absolute;
    left: 330px;
    top: 34px;
    width: 540px;
    height: 780px;
    background: radial-gradient(circle at 60% 35%, var(--cover-grey-light), var(--cover-grey) 70%);
    overflow: hidden;
  }
  .author-photo {
    position: absolute;
    left: 228px;
    top: 210px;
    width: 312px;
    height: 520px;
    background: linear-gradient(160deg, var(--photo-mid) 0%, var(--photo-light) 35%, var(--photo-light) 60%, var(--photo-dark) 100%);
    border-radius: 150px 150px 0 0;
  }
  .testimonial {
    position: absolute;
    top: 44px;
    left: 60px;
    right: 28px;
    text-align: right;
    font-size: 17px;
    letter-spacing: 0.5px;
    line-height: 1.15;
    color: var(--navy);
  }
  .testimonial .source { color: var(--white); }
  .title {
    position: absolute;
    left: 34px;
    top: 104px;
    font-size: 178px;
    line-height: 0.84;
    letter-spacing: -2px;
    color: var(--white);
  }
  .title span { display: block; }
  .title .accent { color: var(--navy); }
  .author-name {
    position: absolute;
    left: 38px;
    top: 590px;
    font-size: 50px;
    line-height: 0.95;
    letter-spacing: 1px;
    color: var(--white);
  }
  .tagline-band {
    position: absolute;
    left: 0;
    right: 0;
    bottom: 0;
    height: 52px;
    background: var(--navy);
    display: flex;
    align-items: center;
    justify-content: center;
    font-size: 24px;
    letter-spacing: 1.5px;
    color: var(--white);
  }
</style>
</head>
<body>
  <main class="book-cover">
    <div class="author-photo" role="img" aria-label="Portrait photo of the author smiling in a white shirt with tattooed forearms"></div>
    <p class="testimonial">“Lorem ipsum dolor sit amet, consectetur adip” <span class="source">-Person reading book</span></p>
    <h1 class="title">
      <span class="accent">TURN</span>
      <span>LUMA</span>
      <span>UP!</span>
    </h1>
    <p class="author-name">MARCUS<br>TILLET</p>
    <p class="tagline-band">A real-life solution to get unstuck and break free</p>
  </main>
</body>
</html>
```